We use a logo that is a sort of smiley face. The mouth is a wrench curved to make the smile. One end of the wrench is a box end and the other is an open end. (These are types of wrenches. If you google combination wrench it will show you) The for the eyes they are hex shaped like nuts (six sides). We want to use this logo and our information for a letterhead that we will use to print invoices. The top right corner needs to have a clean area for the invoice number.
Steadfield Automotive Repair
and Maintenance
48307 Talmin Dr.
Cedarbrook, TX 75512
512-608-4197
www.steadfieldautofix.example
If you can design this information plus the smiley face on there somewhere.
Automotive
Steadfield Automotive Repair and Maintenance

```html
<!DOCTYPE html>
<html lang="en">
<head>
<meta charset="utf-8">
<title>Steadfield Automotive Repair and Maintenance – Letterhead</title>
<link href="https://fonts.googleapis.com/css2?family=Jost:wght@600&display=swap" rel="stylesheet">
<style>
  :root {
    --backdrop: #ffffff;
    --paper: #eaeaeb;
    --navy: #0b1c66;
    --footer-text: #f2f2f4;
  }
  html, body {
    margin: 0;
    padding: 0;
    width: 1200px;
    height: 1000px;
    overflow: hidden;
    background: var(--backdrop);
  }
  .letterhead {
    position: absolute;
    left: 140px;
    top: 12px;
    width: 918px;
    height: 988px;
    background: var(--paper);
    overflow: hidden;
    font-family: "Jost", "Century Gothic", sans-serif;
    font-weight: 600;
  }
  .brand {
    position: absolute;
    left: 52px;
    top: 42px;
    display: flex;
    align-items: center;
    gap: 17px;
    color: var(--navy);
  }
  .brand-dot {
    width: 64px;
    height: 64px;
    border-radius: 50%;
    background: var(--navy);
    flex: none;
  }
  .brand-name {
    font-size: 40px;
    line-height: 1;
    letter-spacing: 0.5px;
    margin: 0;
  }
  .brand-tagline {
    font-size: 10.5px;
    line-height: 1;
    margin: 1px 0 0 1px;
    letter-spacing: 0.3px;
  }
  .footer-band {
    position: absolute;
    left: 0;
    bottom: 0;
    width: 918px;
    height: 100px;
  }
  .footer-band svg {
    position: absolute;
    inset: 0;
    display: block;
  }
  .contact {
    position: relative;
    margin: 0;
    padding-top: 10px;
    text-align: center;
    font-style: normal;
    color: var(--footer-text);
    font-size: 20px;
    line-height: 25px;
    letter-spacing: 1px;
  }
  .contact span { display: block; }
</style>
</head>
<body>
  <main class="letterhead">
    <header class="brand">
      <div class="brand-dot" aria-hidden="true"></div>
      <div class="brand-text">
        <p class="brand-name">STEADFIELD</p>
        <p class="brand-tagline">Automotive Repair and Maintenance</p>
      </div>
    </header>

    <footer class="footer-band">
      <svg width="918" height="100" viewBox="0 0 918 100" aria-hidden="true">
        <ellipse cx="459" cy="140" rx="480" ry="140" fill="var(--navy)"/>
      </svg>
      <address class="contact">
        <span class="contact-phone">512-608-4197</span>
        <span class="contact-web">www.steadfieldautofix.example</span>
        <span class="contact-address">48307 Talmin Dr.Cedarbrook, TX 75512</span>
      </address>
    </footer>
  </main>
</body>
</html>
```